Business Card and Letterhead for Juniper Anvil - (Have Logo)

Update 4: Removed company reg no from business card details as it looked a bit out of place. Updated services list.
UPDATE 3
Sorry, I got the address a little bit wrong, have updated it below. Sorry for any inconvenience caused.
UPDATE 2
Finally I have the details for the business cards and letterhead. Submissions already made do not have to be updated unless shortlisted, if all new submissions could include the details for me, Marcus, that would be very much appreciated and help with the final shortlist selection. I intend to share a shortlist of the three best entries with past and existing customers for their feedback and opinions. Thank you all again for your time.
Here are the details.
Marcus Telby
Web Developer
T: 01632 960 418
E: marcus@juniperanvil.example
www.juniperanvil.example
Professional Photography
Web Solutions & E-Commerce
Audio & HD Video Production
Marketing & Promotions
Identity and Branding
Juniper Anvil Ltd
Suite 20938, 3rd Floor
212-224 Orchard Lane
London, N7 9QX
Company Reg. No: 05829147
The order and the layout of the information are of course down to the design, but the company registration number should be smaller and less prominent. The formatting of the telephone and email address using a T: and an E: I am not sure about and again if it is Tel: or Email: or Icons is up to the design.
The Company No. on the letterhead should read (somewhere in small text along the bottom):
Juniper Anvil is a Ltd Company registered in England & Wales, Registration No. 05829147.
The second business card details are
Oliver Brackley
Photographer
T: 01632 960 418
E: oliver@juniperanvil.example
Everything else the same of course.
Thank you again for all the submissions so far.
END OF UPDATE 2
-
UPDATE 1: Please do not alter the logo nor the logo colours. (This was a previous pixel forum project and I am extremely happy with it. The icon can stand alone of course, but I have had to eliminate all entries that have made it black and white, or reversed the icon.) I would like to thank everyone that has participated so far and am very grateful for all your thought and time.
End of Update 1
-
Original Brief:
I have attached the logo vector file.
Following a superb logo from a previous Pixel Forum project I am now looking for a business card design and (although less important) a letterhead as well.
I must admit I tried to do it myself but could only come up with the usual amateur stuff that in comparison to the quality of the logo looked awful.
About Us
Juniper Anvil Ltd will be a new company due to start in January. It is really just me (a web developer) and my friend (a photographer). We will be aiming at the usual small to medium sized businesses in the local area, selling various digital services including photographic services to the public, web hosting and development, commercial photography, modelling services (not us!), full video and film production and possibly a bit of marketing as well. (Really it is anything we can do professionally all lumped together! We met running seperate businesses which have both since closed)
We will not be competing on price. We plan to be expensive but fair. Certainly not the cheapest.
What we are looking for
Business Card
I imagine a double sided business card, which will be used for more than one person. I imagine the front to be the same for everyone and the persons details to be on the back, although this is of course only my thoughts and I am of course completely open to any ideas.
The card could also have a services list or a bit about what we do on it. It might feature the website address, our business address (mail forwarding address) or our registered company number.
Or it might have none of that, we are completely open to any ideas and have no real fixed opinions. I just want it to be really nice :-)
Letterhead (secondary importance)
We will make our decision primarily on the business card, although a mathcing letterhead would be fantastic. Something standardish in format and simple, although again, all ideas are welcomed.
I hope that is enough information but if you have any questions I will answer them as fully and as quickly as possible.
Thank you once again and I really look forward to seeing your ideas and picking a winner.
Marcus T.
Small businesses AND the general public
Film Production

```html
<!DOCTYPE html>
<html lang="en">
<head>
<meta charset="utf-8">
<title>Juniper Anvil Ltd – Business Card</title>
<link rel="stylesheet" href="https://fonts.googleapis.com/css2?family=Stardos+Stencil:wght@700&display=swap">
<style>
  :root {
    --card-salmon: #ef7d72;
    --card-salmon-light: #f48a80;
    --grain-dark: #d76a60;
    --ink: #2a2220;
    --brand-red: #c4161c;
  }
  html, body {
    margin: 0;
    padding: 0;
    width: 716px;
    height: 1200px;
    overflow: hidden;
    background: var(--card-salmon);
  }
  .card {
    position: relative;
    width: 716px;
    height: 1200px;
    overflow: hidden;
  }
  .wood-surface {
    position: absolute;
    inset: 0;
    background:
      radial-gradient(ellipse 260px 520px at 520px 300px, rgba(180, 80, 75, 0.35), transparent 70%),
      radial-gradient(ellipse 180px 460px at 200px 900px, rgba(170, 85, 85, 0.3), transparent 70%),
      linear-gradient(100deg, var(--card-salmon-light), var(--card-salmon) 45%, var(--grain-dark) 70%, var(--card-salmon));
  }
  .card-face {
    position: absolute;
    top: 0;
    left: 716px;
    width: 1200px;
    height: 716px;
    transform-origin: 0 0;
    transform: rotate(90deg);
    font-family: "Stardos Stencil", "Stencil", serif;
    font-weight: 700;
    color: var(--ink);
    text-transform: uppercase;
  }
  .brand {
    position: absolute;
    left: 56px;
    top: 72px;
    display: flex;
    align-items: center;
    gap: 14px;
    font-size: 40px;
    line-height: 1;
    letter-spacing: 2px;
  }
  .brand-square {
    width: 30px;
    height: 30px;
    background: var(--brand-red);
  }
  .company-details {
    position: absolute;
    left: 604px;
    top: 74px;
    margin: 0;
    font-style: normal;
    font-size: 44px;
    line-height: 54px;
  }
  .company-details .web {
    font-size: 29px;
    line-height: 50px;
  }
  .services {
    position: absolute;
    left: 88px;
    top: 372px;
    margin: 0;
    padding: 0;
    list-style: none;
    font-size: 44px;
    line-height: 54px;
  }
</style>
</head>
<body>
  <div class="card">
    <div class="wood-surface" role="img" aria-label="Salmon pink wood grain texture"></div>
    <div class="card-face">
      <div class="brand">
        <span class="brand-square"></span>
        <span class="brand-name">Juniper Anvil</span>
      </div>
      <address class="company-details">
        <div>Juniper Anvil Ltd</div>
        <div>Suite 20938, 3rd Floor</div>
        <div>212-224 Orchard Lane</div>
        <div>London, N7 9QX</div>
        <div class="web">www.juniperanvil.example</div>
      </address>
      <ul class="services">
        <li>Professional Photography</li>
        <li>Web Solutions &amp; E-Commerce</li>
        <li>Audio &amp; HD Video Production</li>
        <li>Marketing &amp; Promotions</li>
        <li>Identity and Branding</li>
      </ul>
    </div>
  </div>
</body>
</html>
```